New business needs a slick but classy, conservative and elegant Legal Letterhead

We need a new letterhead for a law firm that is slick but very classy and also understated.

The name of the firm is K.L. Marlow Lawyers.

All information about the Law firm should appear at the top of the page. Please no firm information in the footer.

It should have a clean, neat look. No watermarks or bold graphics please.

Info should include the name of the law firm, both the street address and postal address, the phone number and the fax number, the names of the principals, the website. We have attached a word document that contains the relevant information.

We have attached a copy of the business card for further information purposes.

We also need a law society logo to appear (probably on the bottom right hand side of the letterhead?) that states our affiliation to the law society. It is attached and must not be altered in any way. It can be small.

The only footer text we require is as worded in the attached information document.

We would like to see designs that use red and white - in an understated, elegant style - not too modern or too gaudy looking.

The final design should communicate that we mean business and that we are to be trusted.
Updates

Please insert firm's name K.L. Marlow Lawyers on letterhead! I have removed KLM logo as designers were using it instead of the name of the firm. Thank you!

Industry/Entity Type

Legal

Font styles to use
Serif

Colors
ec1f27
ffffff

Requirements
Must have
• All information contained in the word document attached - firm details, law society affiliation logo, firm name & firm logo, principals' names.
Should not have
• watermarks
• no firm details in footer

```html
<!DOCTYPE html>
<html lang="en">
<head>
<meta charset="utf-8">
<title>K.L. Marlow Lawyers – Letterhead</title>
<link rel="stylesheet" href="https://fonts.googleapis.com/css2?family=Arimo:wght@400;700&family=Crimson+Pro:wght@400&display=swap">
<style>
  :root {
    --brand-red: #ec1f27;
    --paper: #ffffff;
    --ink: #222222;
    --shadow: #9a9a9a;
  }
  html, body { margin: 0; padding: 0; overflow: hidden; background: var(--paper); }
  .letterhead {
    position: relative; width: 849px; height: 1200px; overflow: hidden;
    background: var(--paper); font-family: "Crimson Pro", Georgia, serif; color: var(--ink);
  }
  .header-band { position: absolute; left: 0; top: 0; }
  .firm-name {
    position: absolute; left: 26px; top: 22px; margin: 0;
    font-family: "Arimo", Arial, sans-serif; font-weight: 700; font-size: 38px;
    letter-spacing: 0.5px; color: var(--paper);
  }
  .principals {
    position: absolute; left: 26px; top: 78px; margin: 0;
    font-family: "Arimo", Arial, sans-serif; font-size: 17px; color: var(--paper);
  }
  .firm-contact {
    position: absolute; right: 28px; top: 10px; text-align: right;
    font-family: "Arimo", Arial, sans-serif; font-size: 15px; line-height: 19px; color: var(--brand-red);
  }
  .firm-contact p { margin: 0 0 10px; }
  .firm-contact .label { text-decoration: underline; }
  .firm-contact .website { margin-top: 34px; }
  .letter-body {
    position: absolute; left: 108px; top: 272px; width: 630px;
    font-size: 17px; line-height: 22px;
  }
  .letter-body p { margin: 0 0 22px; }
  .letter-body .recipient { margin-bottom: 26px; }
  .letter-body .sign-off { padding-left: 332px; margin-top: 30px; }
  .society-badge { position: absolute; left: 722px; top: 1030px; }
  .footer-band { position: absolute; left: 0; top: 1138px; }
  .footer-note {
    position: absolute; left: 20px; top: 1152px; margin: 0;
    font-family: "Arimo", Arial, sans-serif; font-size: 16px; color: var(--paper);
  }
</style>
</head>
<body>
<div class="letterhead">
  <svg class="header-band" width="849" height="130" viewBox="0 0 849 130" aria-hidden="true">
    <polygon points="0,6 560,6 522,124 0,124" fill="var(--shadow)"/>
    <polygon points="0,0 560,0 522,118 0,118" fill="var(--brand-red)"/>
  </svg>
  <h1 class="firm-name">K.L. MARLOW LAWYERS</h1>
  <p class="principals">Principals: Kieran Marlow &amp; Lena Marlow</p>

  <div class="firm-contact">
    <p><span class="label">Street address:</span><br>Suite 4, 18-26 Harwood Crescent<br>Elmvale NSW 2299</p>
    <p><span class="label">Postal address:</span><br>PO Box 7310<br>Elmvale NSW 2299</p>
    <p>P:(02) 5550 1420<br>F:(02) 5550 1422</p>
    <p class="website">www.klmarlow.example</p>
  </div>

  <div class="letter-body">
    <p class="recipient">Director<br>Rowe &amp; Co<br>12 Fernlea Road<br>Eastbrook<br>Halden HD4 2QT</p>
    <p>Dear Sir or Madam:</p>
    <p>I am writing to you on behalf of the Openleaf project (http://www.openleaf.example), an endeavour to build a fully-fledged multilingual encyclopaedia in an entirely open manner, to ask for permission to use your copyrighted material.</p>
    <p>. . .</p>
    <p>That said, allow me to reiterate that your material will be used to the end of providing a free collection of knowledge for everyone; naturally, only if you agree. If that is the case, could you kindly fill in the attached form and post it back to me? We shall greatly appreciate it.</p>
    <p>Thank you for your time and consideration.</p>
    <p>I look forward to your reply.</p>
    <p class="sign-off">Yours Faithfully,</p>
  </div>

  <svg class="society-badge" width="60" height="60" viewBox="0 0 60 60" role="img" aria-label="Law society membership badge">
    <rect x="0" y="0" width="60" height="60" fill="var(--brand-red)"/>
  </svg>

  <svg class="footer-band" width="849" height="62" viewBox="0 0 849 62" aria-hidden="true">
    <polygon points="0,0 640,0 610,52 0,52" fill="var(--brand-red)"/>
  </svg>
  <p class="footer-note">Liability limited by a scheme approved under Professional Standards</p>
</div>
</body>
</html>
```